We would like a business card that includes our logo on the front and the following information on the back:

Marcus Keene, Owner
Phone: (555) 614-8027
email: mkeenefencing@postvale.net

Marty Keene & Sons Fencing provides the following services:
Barbed wire
Smooth wire
High tensile
Electric

On the bottom of the card please add:
Please call or email Marcus for estimates.

```html
<!DOCTYPE html>
<html lang="en">
<head>
<meta charset="utf-8">
<title>Marty Keene &amp; Sons Fencing – Business Card</title>
<link rel="stylesheet" href="https://fonts.googleapis.com/css2?family=Cinzel:wght@500;600&family=Arimo:wght@400&display=swap">
<style>
  :root {
    --bg: #1d1d1d;
    --brown: #7d5a3f;
    --brown-text: #6b4a30;
    --white: #ffffff;
    --ink: #333333;
    --rule: #8a6a52;
  }
  * { box-sizing: border-box; margin: 0; padding: 0; }
  html, body {
    width: 1200px; height: 1200px; overflow: hidden;
    background: var(--bg);
  }
  .canvas {
    width: 1200px; height: 1200px;
    display: flex; flex-direction: column; align-items: center; justify-content: center;
    gap: 44px;
  }
  .card {
    position: relative;
    width: 960px; height: 548px;
    border-radius: 34px;
    overflow: hidden;
  }
  /* Services side */
  .card-services { background: var(--brown); color: var(--white); }
  .services-heading {
    position: absolute; left: 92px; top: 110px;
    font-family: "Cinzel", serif; font-weight: 600;
    font-size: 30px; line-height: 1.12; letter-spacing: 0.5px;
    width: 440px;
  }
  .services-list {
    position: absolute; left: 100px; top: 262px;
    list-style: none;
    font-family: "Arimo", sans-serif; font-size: 28px; line-height: 44px;
  }
  .services-list li { display: flex; align-items: center; gap: 14px; }
  .services-list svg { width: 22px; height: 22px; flex: none; }
  .fence-art {
    position: absolute; right: 0; bottom: 0;
    width: 400px; height: 340px;
    background: linear-gradient(160deg, #efe7df 0%, #d9c8b8 100%);
    border-top-left-radius: 6px;
  }
  /* Contact side */
  .card-contact { background: var(--white); color: var(--ink); }
  .brand {
    position: absolute; right: 70px; top: 86px;
    display: flex; align-items: center; gap: 14px;
    font-family: "Cinzel", serif; font-weight: 600;
    font-size: 30px; color: var(--ink);
  }
  .brand-mark {
    width: 22px; height: 22px; background: var(--ink); flex: none;
  }
  .person { position: absolute; left: 80px; top: 270px; }
  .person-name {
    font-family: "Cinzel", serif; font-weight: 600;
    font-size: 50px; color: var(--brown-text); letter-spacing: 1px;
  }
  .person-role {
    font-family: "Arimo", sans-serif; font-size: 26px; margin-top: 2px;
  }
  .wire-rule {
    position: absolute; left: 80px; right: 70px; top: 392px;
    height: 2px; background: var(--rule);
  }
  .contact-list {
    position: absolute; left: 80px; top: 418px;
    list-style: none;
    font-family: "Arimo", sans-serif; font-size: 27px; line-height: 42px;
  }
  .contact-list li { display: flex; align-items: center; gap: 14px; }
  .contact-list svg { width: 20px; height: 20px; flex: none; }
  .estimate-note {
    position: absolute; right: 70px; top: 428px;
    font-family: "Arimo", sans-serif; font-size: 22px; color: var(--ink);
  }
  .estimate-note .accent { color: var(--brown-text); }
</style>
</head>
<body>
<main class="canvas">

  <section class="card card-services">
    <h2 class="services-heading">Marty Keene &amp; Sons Fencing provides the following services:</h2>
    <ul class="services-list">
      <li><svg viewBox="0 0 22 22"><circle cx="11" cy="11" r="11" fill="#fff"/><path d="M6 11.5l3.2 3.2L16 8" stroke="#7d5a3f" stroke-width="2.6" fill="none" stroke-linecap="round" stroke-linejoin="round"/></svg>Barbed Wire</li>
      <li><svg viewBox="0 0 22 22"><circle cx="11" cy="11" r="11" fill="#fff"/><path d="M6 11.5l3.2 3.2L16 8" stroke="#7d5a3f" stroke-width="2.6" fill="none" stroke-linecap="round" stroke-linejoin="round"/></svg>Smooth Wire</li>
      <li><svg viewBox="0 0 22 22"><circle cx="11" cy="11" r="11" fill="#fff"/><path d="M6 11.5l3.2 3.2L16 8" stroke="#7d5a3f" stroke-width="2.6" fill="none" stroke-linecap="round" stroke-linejoin="round"/></svg>High Tensile</li>
      <li><svg viewBox="0 0 22 22"><circle cx="11" cy="11" r="11" fill="#fff"/><path d="M6 11.5l3.2 3.2L16 8" stroke="#7d5a3f" stroke-width="2.6" fill="none" stroke-linecap="round" stroke-linejoin="round"/></svg>Electric</li>
    </ul>
    <div class="fence-art" role="img" aria-label="Large white illustration of wooden fence posts strung with barbed wire"></div>
  </section>

  <section class="card card-contact">
    <div class="brand">
      <span class="brand-mark"></span>
      <span class="brand-name">Marty Keene &amp; Sons Fencing</span>
    </div>
    <div class="person">
      <h1 class="person-name">MARCUS KEENE</h1>
      <p class="person-role">Owner</p>
    </div>
    <div class="wire-rule"></div>
    <ul class="contact-list">
      <li><svg viewBox="0 0 20 20"><path d="M5 2l3 3.5-1.8 2.2c1 2.3 2.8 4.1 5.1 5.1l2.2-1.8L17 14l-2 3.5C8.5 17 3 11.5 2.5 5z" fill="#7d5a3f"/></svg>(555) 614-8027</li>
      <li><svg viewBox="0 0 20 20"><rect x="1.5" y="4" width="17" height="12" fill="none" stroke="#7d5a3f" stroke-width="2"/><path d="M2 5l8 6 8-6" fill="none" stroke="#7d5a3f" stroke-width="2"/></svg>mkeenefencing@postvale.net</li>
    </ul>
    <p class="estimate-note">Please call or email <span class="accent">Marcus for estimates.</span></p>
  </section>

</main>
</body>
</html>
```